Learn-to-Swim Program for Children's Day Camp (Walter Brightley Fieldgrounds)

We are a children's camp with a robust swim instruction program and we need a series of 5 kid-friendly banners which list the skills learned in our swim program that can be hung up around each outdoor pool complex. All together there are 6 overarching levels and 12 sublevels (see attached). Except for the Level V & VI, each banner should be one overarching level and the 2-3 sublevels that define it.

Each swim level has a name, most of which are sea creatures, and we want to have a corresponding image/avatar to go with the swim level name (e.g. tadpole, barracuda, orca, goldfish, catfish).

The banners should be 3 feet (width) by 5 feet (height). The banners will be hung outdoors so it needs a color scheme that won't get lost in the sunlight.

We will want to include our logo but do not need the design to match our logo colors. Logo can be in black or white.

Our website is: www.campwbf.example

Target Market(s)

children age 5 - 12

Industry/Entity Type

children's day camp

Requirements
Must have
• A progression from level I to level VI. Should have a happy, bright, fun, tone, text MUST be legible from at least a 5 foot distance
Should not have
• adult themes, a scheme that evokes sadness or fear

```html
<!DOCTYPE html>
<html lang="en">
<head>
<meta charset="utf-8">
<title>Level Skills Banner – Walter Brightley Fieldgrounds</title>
<link href="https://fonts.googleapis.com/css2?family=Poppins:wght@500;600;700;800&display=swap" rel="stylesheet">
<style>
  :root {
    --page-bg: #eceef0;
    --panel-blue: #0c58a9;
    --band-blue: #1649a6;
    --band-deep: #24389a;
    --skill-green: #3bb443;
    --sun-yellow: #f3dd14;
    --meadow-green: #45b43a;
    --pool-light: #5fd0cf;
    --pool-deep: #0f7f9a;
    --white: #ffffff;
  }
  html, body {
    margin: 0;
    padding: 0;
    width: 1200px;
    height: 2666px;
    overflow: hidden;
    background: var(--page-bg);
  }
  .banner {
    position: absolute;
    left: 40px;
    top: 398px;
    width: 1120px;
    height: 1870px;
    box-shadow: 0 6px 18px rgba(0,0,0,0.18);
  }
  .banner svg { display: block; width: 100%; height: 100%; }
  .type { font-family: 'Poppins', sans-serif; }
  .brand-name { fill: var(--white); font-weight: 700; font-size: 13.5px; letter-spacing: 0.4px; }
  .title-level { fill: var(--white); font-weight: 700; font-size: 46px; }
  .title-skills { fill: var(--skill-green); font-weight: 800; font-size: 70px; }
  .level-name { fill: var(--white); font-weight: 700; font-size: 25px; }
  .skill { fill: var(--white); font-weight: 500; font-size: 17.5px; }
  .moveup-label { fill: var(--sun-yellow); font-weight: 700; font-size: 21px; }
  .moveup-text { fill: var(--skill-green); font-weight: 600; font-size: 16.5px; }
</style>
</head>
<body>
  <div class="banner">
    <svg viewBox="0 0 674 1125" xmlns="http://www.w3.org/2000/svg">
      <defs>
        <linearGradient id="poolWater" x1="0" y1="0" x2="0.3" y2="1">
          <stop offset="0" stop-color="var(--pool-light)"/>
          <stop offset="0.55" stop-color="#2bb3bd"/>
          <stop offset="1" stop-color="var(--pool-deep)"/>
        </linearGradient>
        <linearGradient id="sunMeadow" x1="0" y1="0" x2="0" y2="1">
          <stop offset="0" stop-color="var(--sun-yellow)"/>
          <stop offset="0.45" stop-color="#bfd62a"/>
          <stop offset="1" stop-color="var(--meadow-green)"/>
        </linearGradient>
      </defs>

      <!-- hero photo area -->
      <rect class="hero-photo" x="0" y="0" width="674" height="510" fill="url(#poolWater)"
            role="img" aria-label="Photo of a smiling child swimming underwater in a pool, reaching toward the camera, with another child behind"/>

      <!-- brand name -->
      <g class="brand">
        <rect x="392" y="136" width="10" height="10" fill="var(--white)"/>
        <text class="type brand-name" x="655" y="146" text-anchor="end">WALTER BRIGHTLEY FIELDGROUNDS</text>
      </g>

      <!-- blue content field -->
      <polygon class="content-field" points="0,438 674,500 674,1125 0,1125" fill="var(--panel-blue)"/>

      <!-- side panels -->
      <polygon class="side-panel side-left" points="0,468 83,478 83,1125 0,1125" fill="url(#sunMeadow)"/>
      <polygon class="side-panel side-right" points="571,530 674,522 674,1125 571,1125" fill="url(#sunMeadow)"/>

      <!-- heading -->
      <text class="type" x="134" y="550">
        <tspan class="title-level">LEVEL </tspan><tspan class="title-skills" dx="2">SKILLS</tspan>
      </text>

      <!-- Wader -->
      <text class="type level-name" x="98" y="608">WADER</text>
      <g class="skill-list">
        <text class="type skill" x="105" y="640">• Gets into the water with assistance</text>
        <text class="type skill" x="105" y="671">• Follows pool rules</text>
        <text class="type skill" x="105" y="702">• Can hold big breath and get chin/ cheeks in water</text>
        <text class="type skill" x="105" y="733">• Cups hands to hold water and get some of face wet</text>
        <text class="type skill" x="105" y="764">• Doesn’t always need assistance in water</text>
      </g>
      <rect class="moveup-band" x="83" y="790" width="488" height="40" fill="var(--band-blue)"/>
      <text class="type" x="98" y="816">
        <tspan class="moveup-label">Move-Up: </tspan><tspan class="moveup-text">Must be comfortable entering the water</tspan>
      </text>

      <!-- Splasher -->
      <text class="type level-name" x="98" y="870">SPLASHER</text>
      <g class="skill-list">
        <text class="type skill" x="105" y="902">• Enters and exits pool without assistance</text>
        <text class="type skill" x="105" y="933">• Can do a slide in entry</text>
        <text class="type skill" x="105" y="964">• Plays in water up to chest deep</text>
        <text class="type skill" x="105" y="995">• Dips face and head in water</text>
        <text class="type skill" x="105" y="1026">• Blows bubbles through the mouth</text>
      </g>
      <rect class="moveup-band" x="83" y="1050" width="488" height="75" fill="var(--band-deep)"/>
      <text class="type moveup-label" x="98" y="1075">Move-Up:</text>
      <text class="type moveup-text" x="213" y="1074">Must fully submerge body and head</text>
      <text class="type moveup-text" x="213" y="1094">underwater (no nose holding)</text>
    </svg>
  </div>
</body>
</html>
```